Construction business card

I need a new business card, they can connect with my logo, brand.
What we do is residential house , design and build
I like: Navy blue / black
I attached our logo, brand,
and, some idea for business card.

```html
<!DOCTYPE html>
<html lang="en">
<head>
<meta charset="utf-8">
<title>Harlow Building Group – Business Card</title>
<link rel="stylesheet" href="https://fonts.googleapis.com/css2?family=Oswald:wght@400;600&display=swap">
<style>
  :root {
    --backdrop: #2f3133;
    --card-black: #1e1e1e;
    --brand-blue: #3a82cd;
    --brand-blue-deep: #1f5fa6;
    --ink-white: #ffffff;
  }
  * { box-sizing: border-box; margin: 0; padding: 0; }
  html, body {
    width: 1200px; height: 939px; overflow: hidden;
    background: var(--backdrop);
    font-family: "Oswald", sans-serif;
  }
  .canvas { position: relative; width: 1200px; height: 939px; }
  .card {
    position: absolute;
    width: 560px; height: 320px;
    border-radius: 3px;
    box-shadow: 0 14px 30px rgba(0,0,0,.45);
  }
  .card--front {
    left: 90px; top: 110px;
    background: var(--card-black);
    display: flex; align-items: center; justify-content: center;
  }
  .card--back {
    left: 550px; top: 500px;
    background: var(--brand-blue);
  }
  .wordmark {
    display: flex; align-items: center; gap: 14px;
    font-weight: 600; text-transform: uppercase; letter-spacing: 1px;
  }
  .wordmark__square { width: 22px; height: 22px; background: var(--brand-blue); }
  .wordmark__name { font-size: 34px; line-height: 1.05; color: var(--ink-white); }
  .card--back .wordmark {
    position: absolute; right: 34px; top: 112px;
    flex-direction: column; align-items: flex-end; gap: 10px;
  }
  .card--back .wordmark__square { background: var(--brand-blue-deep); }
  .card--back .wordmark__name { color: var(--brand-blue-deep); font-size: 30px; text-align: right; }
  .contact {
    position: absolute; left: 36px; top: 96px;
    color: var(--ink-white);
  }
  .contact__name { font-size: 26px; font-weight: 600; text-transform: uppercase; letter-spacing: .5px; }
  .contact__role { font-size: 14px; font-weight: 400; margin-top: 2px; }
  .contact__line { font-size: 14px; font-weight: 400; line-height: 1.5; }
  .contact__list { list-style: none; margin-top: 4px; }
  .contact__item { display: flex; align-items: center; gap: 9px; font-size: 14px; line-height: 1.6; }
  .contact__icon { width: 14px; height: 14px; flex: none; }
</style>
</head>
<body>
<main class="canvas">
  <section class="card card--front">
    <div class="wordmark">
      <span class="wordmark__square"></span>
      <span class="wordmark__name">Harlow<br>Building Group</span>
    </div>
  </section>

  <section class="card card--back">
    <div class="contact">
      <p class="contact__name">Daniel Reyes</p>
      <p class="contact__role">Director</p>
      <p class="contact__line">HARLOW BUILDING GROUP PTY LTD</p>
      <p class="contact__line">ABN: 48 302 551 716</p>
      <ul class="contact__list">
        <li class="contact__item">
          <svg class="contact__icon" viewBox="0 0 14 14"><rect x="3" y="1" width="8" height="12" rx="1.5" fill="none" stroke="#fff" stroke-width="1.4"/><rect x="6" y="10.5" width="2" height="1" fill="#fff"/></svg>
          0400 555 218
        </li>
        <li class="contact__item">
          <svg class="contact__icon" viewBox="0 0 14 14"><rect x="1" y="3" width="12" height="8" fill="#fff"/><path d="M1 3l6 5 6-5" fill="none" stroke="#3a82cd" stroke-width="1.2"/></svg>
          info@harlowbuilding.com.au
        </li>
        <li class="contact__item">
          <svg class="contact__icon" viewBox="0 0 14 14"><path d="M7 13S2.5 8 2.5 5.5a4.5 4.5 0 0 1 9 0C11.5 8 7 13 7 13z" fill="#fff"/><circle cx="7" cy="5.5" r="1.7" fill="#3a82cd"/></svg>
          27 Example St, Springvale, VIC 3171
        </li>
        <li class="contact__item">
          <svg class="contact__icon" viewBox="0 0 14 14"><circle cx="7" cy="7" r="5.8" fill="none" stroke="#fff" stroke-width="1.2"/><ellipse cx="7" cy="7" rx="2.5" ry="5.8" fill="none" stroke="#fff" stroke-width="1"/><path d="M1.2 7h11.6" stroke="#fff" stroke-width="1"/></svg>
          www.harlowbuilding.com.au
        </li>
      </ul>
    </div>
    <div class="wordmark">
      <span class="wordmark__square"></span>
      <span class="wordmark__name">Harlow<br>Building Group</span>
    </div>
  </section>
</main>
</body>
</html>
```